Advertisements for web banners and street signage

Role Finch is a New Zealand Job Board (career vacancy search) website that requires some creative ad banners for promotion online, at events, and on street signage.

Our role finch logo is attached in low resolution, and in high resolution, the logo, slogan, and website should be incorporated somewhere in the ad. Ads should be long in length (not square) either vertical or horizontal.

I've attached some examples of ads

Target Market(s)

Working population. We exist to bring more choice to New Zealand job seekers and save job seekers time. We are about "finding your next job"

Industry/Entity Type

Recruitment

Requirements
Must have
• Use of bright colours. Gets your attention.
Nice to have
• A funny image or joke related to finding a job that catches your attention e.g. could play on the use of Role Finch = job "sauce"
• A slogan, pun, or sentence related to finding a job that catches your attention, An example of a slogans "some say a change is as good as a holiday"
Should not have
• Swearing or sexism

```html
<!DOCTYPE html>
<html lang="en">
<head>
<meta charset="UTF-8">
<title>Role Finch – Find a new job to complain about</title>
<link href="https://fonts.googleapis.com/css2?family=Montserrat:wght@400;600;700;800;900&display=swap" rel="stylesheet">
<style>
  :root {
    --ink: #323c42;
    --teal: #17b3a5;
    --paper: #ffffff;
    --mist: #e4f6f3;
    --grey: #6b7277;
    --skin: #e9a57d;
    --shirt: #dff2f4;
  }
  * { margin: 0; padding: 0; box-sizing: border-box; }
  html, body { width: 945px; height: 1200px; overflow: hidden; }
  body { font-family: "Montserrat", sans-serif; color: var(--ink); }

  .poster {
    position: relative;
    width: 945px;
    height: 1200px;
    overflow: hidden;
    background: linear-gradient(120deg, var(--paper) 40%, var(--mist) 100%);
  }

  .brand-disc {
    position: absolute;
    left: 644px; top: -65px;
    width: 330px; height: 330px;
    border-radius: 50%;
    background: var(--paper);
  }
  .brand {
    position: absolute;
    left: 644px; top: 140px;
    width: 330px;
    text-align: center;
  }
  .brand-name {
    font-size: 30px;
    font-weight: 600;
    letter-spacing: 2px;
    color: var(--ink);
  }
  .brand-slogan {
    margin-top: 4px;
    font-size: 9px;
    font-weight: 600;
    letter-spacing: 1.6px;
    color: var(--grey);
  }

  .teaser {
    position: absolute;
    left: 50px; top: 52px;
    font-size: 39px;
    font-weight: 800;
    line-height: 1.14;
  }

  .headline {
    position: absolute;
    left: 46px; top: 232px;
    font-size: 119px;
    font-weight: 900;
    line-height: 115px;
    letter-spacing: -2px;
  }
  .headline .accent { color: var(--teal); }

  .blurb {
    position: absolute;
    left: 45px; top: 740px;
    width: 560px;
    font-size: 18px;
    line-height: 26px;
    font-weight: 400;
  }

  .call {
    position: absolute;
    left: 45px; top: 908px;
    font-size: 39px;
    font-weight: 800;
    line-height: 50px;
  }

  .figure-art {
    position: absolute;
    left: 642px; top: 622px;
    width: 303px; height: 450px;
    border-radius: 150px 150px 0 0;
    background: linear-gradient(180deg, #b9713a 0%, var(--skin) 30%, var(--shirt) 62%, #f3c23c 100%);
  }

  .footer {
    position: absolute;
    left: 0; top: 1072px;
    width: 945px; height: 128px;
    background: var(--ink);
  }
  .footer-bars { position: absolute; left: 0; top: 0; }
  .site {
    position: absolute;
    left: 0; top: 0;
    width: 945px; height: 128px;
    display: flex; align-items: center; justify-content: center;
    font-size: 46px;
    font-weight: 400;
    letter-spacing: 2px;
    color: var(--paper);
  }
</style>
</head>
<body>
  <div class="poster">
    <div class="brand-disc"></div>
    <div class="brand">
      <div class="brand-name">ROLE FINCH</div>
      <div class="brand-slogan">FINDING YOUR NEXT JOB</div>
    </div>

    <p class="teaser">TIRED OF BEING<br>STUCK IN YOUR OLD,<br>DISSATISFYING JOB?</p>

    <h1 class="headline">
      FIND A<br>
      <span class="accent">NEW</span> JOB TO<br>
      <span class="accent">COMPLAIN</span><br>
      ABOUT!
    </h1>

    <p class="blurb">Far far away, behind the word mountains,<br>far from the countries Vokalia and Consonantia,<br>there live the blind texts. Separated they live in<br>Bookmarksgrove right at the coast of the<br>Semantics, a large language ocean.</p>

    <p class="call">CALL US NOW!<br>0800-555-0147</p>

    <div class="figure-art" role="img" aria-label="Cartoon of a grumpy office worker with a moustache, shirt and yellow striped tie"></div>

    <footer class="footer">
      <svg class="footer-bars" width="945" height="128" viewBox="0 0 945 128" aria-hidden="true">
        <g fill="var(--teal)">
          <rect x="0" y="20" width="77" height="26"/>
          <rect x="45" y="55" width="65" height="26"/>
          <rect x="85" y="88" width="45" height="19"/>
          <rect x="868" y="20" width="77" height="26"/>
          <rect x="832" y="55" width="73" height="26"/>
          <rect x="815" y="88" width="45" height="19"/>
        </g>
      </svg>
      <div class="site">www.rolefinch.co.nz</div>
    </footer>
  </div>
</body>
</html>
```